Business Card for Beach theme sports bar called TAVRU

I need a business card designed for our employees, front and back. This will be used by the employees of two business locations to hand out to customers. I've attached the previous business cards we used at one time for a Benwicks (it is now Tavru). Looking for a fresh new card that is elegant but has character.

Target Market(s)

30-60, middle class

Contact Information for Business Card

We are a beach bar and sports bar. I am looking for an elegant business card with the front to have the TAVRU logo. Then on the back I need it to allow a space for employees to write their names and for them to write in their schedule. I have attached our old cards with our old name Benwicks so you can pull everything we need on the cards. one thing is missing is we have another location at 2815 N Willow Crest Rd with a number of 702-418-9351. Since we will use it for both locations it should allow the employee to circle or check mark the bar which they work at.

Font styles to use
Sans Serif

Requirements
Must have
• We are looking for some fresh ideas for the business card. Something that will really stick out to customers when the staff hands them out. Creativity will be looked at positively, but we still want it to look upscale and fun.

```html
<!DOCTYPE html>
<html lang="en">
<head>
<meta charset="utf-8">
<title>Tavru Business Card</title>
<link rel="stylesheet" href="https://fonts.googleapis.com/css2?family=Work+Sans:wght@400;500&display=swap">
<style>
  :root {
    --stage: #1c1c1c;
    --card-dark: #111111;
    --card-light: #ffffff;
    --ink: #1a1a1a;
    --ink-soft: #555555;
    --rule: #9a9a9a;
    --paper-ink: #f2f2f2;
  }
  * { box-sizing: border-box; margin: 0; padding: 0; }
  html, body { width: 1200px; height: 900px; overflow: hidden; }
  body {
    background: var(--stage);
    font-family: "Work Sans", sans-serif;
    display: flex;
    flex-direction: column;
    align-items: center;
    justify-content: center;
    gap: 44px;
  }
  .card {
    width: 630px;
    height: 360px;
    position: relative;
    box-shadow: 0 12px 30px rgba(0,0,0,0.45);
  }
  .card--front {
    background: linear-gradient(135deg, #151515 0%, var(--card-dark) 60%, #1d1d1d 100%);
    display: flex;
    align-items: center;
    justify-content: center;
  }
  .brand {
    display: flex;
    align-items: center;
    gap: 14px;
    font-weight: 500;
    letter-spacing: 0.08em;
  }
  .brand__dot { width: 16px; height: 16px; border-radius: 50%; }
  .card--front .brand { color: var(--paper-ink); font-size: 44px; }
  .card--front .brand__dot { background: var(--paper-ink); }

  .card--back {
    background: var(--card-light);
    display: flex;
    align-items: center;
  }
  .brand-area {
    width: 250px;
    display: flex;
    justify-content: center;
  }
  .card--back .brand { color: var(--ink); font-size: 36px; gap: 12px; }
  .card--back .brand__dot { background: var(--ink); width: 14px; height: 14px; }
  .divider { width: 2px; height: 290px; background: var(--ink); }

  .details { padding-left: 30px; width: 376px; color: var(--ink); }
  .label {
    font-size: 11px;
    font-weight: 500;
    letter-spacing: 0.12em;
    color: var(--ink-soft);
  }
  .write-in {
    display: flex;
    align-items: flex-end;
    gap: 10px;
    margin-bottom: 14px;
  }
  .write-in__line { flex: 1; height: 22px; border-bottom: 1px solid var(--ink); }
  .schedule { margin-bottom: 14px; }
  .schedule__grid {
    display: grid;
    grid-template-columns: repeat(7, 1fr);
    border: 1px solid var(--ink);
    margin-top: 6px;
  }
  .schedule__day {
    border-left: 1px solid var(--rule);
    font-size: 10px;
    font-weight: 500;
    text-align: center;
    padding-top: 3px;
    height: 38px;
  }
  .schedule__day:first-child { border-left: none; }
  .locations { list-style: none; margin-bottom: 10px; }
  .location {
    display: flex;
    align-items: flex-start;
    gap: 10px;
    font-size: 13px;
    line-height: 1.35;
    margin-bottom: 8px;
  }
  .location__box {
    width: 13px; height: 13px; flex: none;
    border: 1.5px solid var(--ink);
    margin-top: 2px;
  }
  .location__phone { display: flex; align-items: center; gap: 6px; }
  .contact__list { list-style: none; display: flex; gap: 18px; }
  .contact__item { display: flex; align-items: center; gap: 7px; font-size: 13px; }
  svg { width: 11px; height: 11px; flex: none; }
</style>
</head>
<body>
  <section class="card card--front">
    <div class="brand"><span class="brand__dot"></span>TAVRU</div>
  </section>

  <section class="card card--back">
    <div class="brand-area">
      <div class="brand"><span class="brand__dot"></span>TAVRU</div>
    </div>
    <div class="divider"></div>
    <div class="details">
      <div class="write-in">
        <span class="label">NAME</span>
        <span class="write-in__line"></span>
      </div>

      <div class="schedule">
        <span class="label">MY SCHEDULE</span>
        <div class="schedule__grid">
          <span class="schedule__day">MON</span>
          <span class="schedule__day">TUE</span>
          <span class="schedule__day">WED</span>
          <span class="schedule__day">THU</span>
          <span class="schedule__day">FRI</span>
          <span class="schedule__day">SAT</span>
          <span class="schedule__day">SUN</span>
        </div>
      </div>

      <ul class="locations">
        <li class="location">
          <span class="location__box"></span>
          <div>
            <p>148 Harbor Lane, Las Vegas, NV</p>
            <p class="location__phone">
              <svg viewBox="0 0 12 12" aria-hidden="true"><path d="M2.5 1 L4.5 1 L5 3.5 L3.8 4.4 Q5 7 7.6 8.2 L8.5 7 L11 7.5 L11 9.5 Q11 11 9.5 11 Q1 10 1 2.5 Q1 1 2.5 1 Z" fill="#1a1a1a"/></svg>
              (702) 555-0147
            </p>
          </div>
        </li>
        <li class="location">
          <span class="location__box"></span>
          <div>
            <p>2815 N Willow Crest Rd, Las Vegas, NV</p>
            <p class="location__phone">
              <svg viewBox="0 0 12 12" aria-hidden="true"><path d="M2.5 1 L4.5 1 L5 3.5 L3.8 4.4 Q5 7 7.6 8.2 L8.5 7 L11 7.5 L11 9.5 Q11 11 9.5 11 Q1 10 1 2.5 Q1 1 2.5 1 Z" fill="#1a1a1a"/></svg>
              702-418-9351
            </p>
          </div>
        </li>
      </ul>

      <ul class="contact__list">
        <li class="contact__item">
          <svg viewBox="0 0 12 12" aria-hidden="true"><rect x="1" y="2.5" width="10" height="7" fill="none" stroke="#1a1a1a" stroke-width="1.2"/><path d="M1 2.5 L6 6.5 L11 2.5" fill="none" stroke="#1a1a1a" stroke-width="1.2"/></svg>
          info@tavru.com
        </li>
        <li class="contact__item">
          <svg viewBox="0 0 12 12" aria-hidden="true"><circle cx="6" cy="6" r="5" fill="none" stroke="#1a1a1a" stroke-width="1.1"/><ellipse cx="6" cy="6" rx="2.2" ry="5" fill="none" stroke="#1a1a1a" stroke-width="1"/><path d="M1 6 H11" stroke="#1a1a1a" stroke-width="1"/></svg>
          www.tavru.com
        </li>
      </ul>
    </div>
  </section>
</body>
</html>
```